Brightfold Partners Website

Brightfold Partners (BP) provide Analytics & Enterprise Performance Management (EPM) advisory & consultancy services. We are passionate about data and making a difference for our clients by working in partnership with them, helping them on their journey to becoming an Brightfold Partner. We deliver insights which give our clients a competitive edge and a much deeper understanding of their organisation.

We need a website which shows who we are, what we do and how we do it.

www.brightfold-partners.example is our very basic website at the moment. We want to completely revamp it with a corporate look

```html
<!DOCTYPE html>
<html lang="en">
<head>
<meta charset="utf-8">
<title>Brightfold Partners — Data Analytics &amp; EPM Consulting</title>
<link href="https://fonts.googleapis.com/css2?family=Fira+Sans:wght@500;600;700&family=Roboto:wght@400;500;700&display=swap" rel="stylesheet">
<style>
:root{
  --orange:#e0865a;
  --orange-bright:#f08a1c;
  --red:#e3432e;
  --navy:#2c5574;
  --ink:#2a2a2a;
  --text:#555a60;
  --muted:#8a8f95;
  --line:#d9dcdf;
  --pale:#f4f4f4;
  --white:#ffffff;
}
*{margin:0;padding:0;box-sizing:border-box}
html,body{width:1200px;height:3790px;overflow:hidden;background:var(--white)}
body{font-family:"Roboto",sans-serif;color:var(--text);position:relative}
.page{position:relative;width:1200px;height:3790px;overflow:hidden}
.abs{position:absolute}
svg{flex:none}
h1,h2,h3,h4{font-family:"Fira Sans",sans-serif;color:var(--navy);font-weight:600}
a{color:inherit;text-decoration:none}

/* top bar */
.topbar{top:0;left:0;width:1200px;height:46px;background:var(--navy)}
.topbar-left{position:absolute;top:0;left:0;width:500px;height:46px;background:var(--orange);clip-path:polygon(0 0,100% 0,96% 100%,0 100%)}
.topbar-item{position:absolute;top:15px;font-size:14px;line-height:16px;color:var(--white);display:flex;align-items:center;gap:9px;white-space:nowrap}
.topbar-item svg{width:13px;height:13px;fill:var(--white)}
.topbar-sep{position:absolute;top:13px;left:1052px;width:1px;height:20px;background:rgba(255,255,255,.6)}
.topbar-soc{position:absolute;top:17px;width:12px;height:12px;background:var(--white);border-radius:2px}

/* header */
.header{top:46px;left:0;width:1200px;height:98px;background:var(--white)}
.brand{display:flex;align-items:center;gap:12px}
.brand .dot{width:62px;height:62px;border-radius:50%;background:var(--navy)}
.brand .name{font-family:"Fira Sans",sans-serif;font-weight:600;color:var(--navy);font-size:22px;line-height:25px;letter-spacing:.5px}
.nav{top:41px;left:531px;display:flex;gap:34px;font-size:14px;color:var(--navy)}
.nav .active{color:var(--orange)}
.round-btn{top:30px;width:37px;height:37px;border:1.5px solid var(--ink);border-radius:50%;display:flex;align-items:center;justify-content:center}
.band{top:144px;left:0;width:1200px;height:15px;background:var(--orange)}

/* hero */
.hero{top:159px;left:0;width:1200px;height:567px;background:linear-gradient(90deg,#dfe5ea 0%,#e6ebef 45%,#c9d3db 100%)}
.hero-photo{top:0;left:590px;width:610px;height:567px;background:linear-gradient(160deg,#a9b8c4 0%,#6f8394 45%,#3f5566 100%);clip-path:polygon(10% 0,100% 0,100% 100%,0 100%)}
.hero .kicker{top:122px;left:85px;font-size:17px;color:var(--navy)}
.hero h1{top:148px;left:85px;font-size:47px;line-height:54px}
.rule{height:3px;background:var(--orange)}
.hero p{top:294px;left:85px;width:520px;font-size:15px;line-height:23px;color:var(--ink)}
.play{width:46px;height:46px;border-radius:50%;background:var(--white);display:flex;align-items:center;justify-content:center}
.btn{background:var(--orange);color:var(--white);font-size:14px;font-weight:500;display:flex;align-items:center;justify-content:center;border-radius:2px}

/* about */
.about-back{top:836px;left:220px;width:329px;height:328px;background:linear-gradient(135deg,#1c3d8a,#3a6fd0 60%,#0f2660)}
.about-front{top:976px;left:85px;width:340px;height:282px;background:var(--white);padding:8px;box-shadow:0 6px 20px rgba(0,0,0,.12)}
.about-front div{width:100%;height:100%;background:linear-gradient(135deg,#e9eef3,#b7c3cf 60%,#5d6b78)}
.play-sq{top:1141px;left:398px;width:45px;height:45px;background:var(--orange);display:flex;align-items:center;justify-content:center;box-shadow:6px 6px 0 #cfcfcf}
.label{font-size:14px;color:var(--orange);display:flex;align-items:center;gap:10px}
.label::after{content:"";width:28px;height:2px;background:var(--orange)}
.section-h{font-size:43px;line-height:46px}
.body-text{font-size:13.5px;line-height:21px;color:var(--text)}
.btn-outline{border:1.5px solid var(--orange);color:var(--orange);font-size:14px;display:flex;align-items:center;justify-content:center;border-radius:3px}
.partner{display:flex;align-items:center;gap:12px;font-weight:700;font-size:15px;color:var(--ink)}
.partner .bar{width:2px;height:30px;background:var(--ink)}

/* services */
.services{top:1367px;left:0;width:1200px;height:823px;background:var(--pale)}
.card{top:1582px;width:325px;height:500px;background:var(--white)}
.card .img{position:absolute;top:22px;left:18px;width:288px;height:209px}
.card .ico{position:absolute;top:196px;left:222px;width:64px;height:64px;border-radius:50%;background:var(--white);box-shadow:0 3px 10px rgba(0,0,0,.1);display:flex;align-items:center;justify-content:center}
.card h3{position:absolute;top:256px;left:36px;font-size:19px;line-height:26px}
.card p{position:absolute;top:320px;left:36px;width:250px;font-size:13px;line-height:21px;color:var(--text)}
.card .more{position:absolute;top:420px;left:36px;width:260px;height:45px;background:var(--pale);font-size:14px;font-weight:500;color:var(--navy);padding:15px 0 0 20px}
.card .more span{position:absolute;right:0;top:0;width:56px;height:45px;background:var(--navy);clip-path:polygon(20% 0,100% 0,100% 100%,0 100%);display:flex;align-items:center;justify-content:center}

/* process */
.process{top:2190px;left:0;width:1200px;height:559px;background:var(--ink);overflow:hidden}
.process-side{top:0;left:0;width:453px;height:559px;background:linear-gradient(90deg,var(--orange-bright),var(--red))}
.process-img{top:66px;left:85px;width:449px;height:428px;background:linear-gradient(160deg,#eef2f6,#b8c7d8 55%,#7f93ad)}
.process h2{color:var(--white)}
.step{left:587px;width:526px;display:flex;gap:20px;font-size:16px;line-height:24px;color:#dcdcdc;letter-spacing:.3px}
.step .num{position:relative;width:26px;height:40px;flex:none}
.step .num i{position:absolute;top:8px;left:0;width:24px;height:24px;border-radius:50%;background:var(--orange)}
.step .num b{position:absolute;top:8px;left:14px;font-family:"Fira Sans",sans-serif;font-size:28px;font-weight:600;color:var(--white)}
.step-line{left:587px;width:526px;height:1px;background:rgba(255,255,255,.45)}
.deco{border-radius:50%;background:#3a3a3a}

/* contact */
.contact-item{left:85px;display:flex;gap:20px;font-size:14px;line-height:21px;color:var(--navy)}
.contact-item svg{width:24px;height:24px;fill:var(--orange);margin-top:2px}
.form{top:2859px;left:525px;width:588px;height:413px;background:var(--white);box-shadow:0 4px 26px rgba(0,0,0,.08)}
.form h3{position:absolute;top:44px;left:44px;font-size:23px}
.form .rule{position:absolute;top:92px;left:44px;width:28px;height:2px}
.field{position:absolute;width:244px;height:32px;border-bottom:1px solid var(--line);font-size:13px;color:var(--muted)}
.form .send{position:absolute;top:323px;left:44px;width:120px;height:46px}

/* footer */
.footer{top:3381px;left:0;width:1200px;height:409px;background:var(--navy)}
.footer .brand .dot{width:44px;height:44px;background:var(--white)}
.footer .brand .name{color:var(--white);font-size:16px;line-height:19px}
.footer p{font-size:14px;line-height:21px;color:var(--white)}
.footer h4{font-size:20px;color:var(--white)}
.flink{font-size:13.5px;color:var(--white);display:flex;gap:12px;align-items:center}
.flink::before{content:"»";color:#8fa6b8;font-size:13px}
.fsq{width:41px;height:41px;background:#5a7a92}
.copy-line{top:3718px;left:0;width:1200px;height:1px;background:rgba(255,255,255,.25)}
.copy{top:3740px;left:0;width:1200px;text-align:center;font-size:13.5px;color:var(--white)}
.copy span{color:var(--orange)}
</style>
</head>
<body>
<div class="page">

  <!-- top bar -->
  <div class="abs topbar">
    <div class="topbar-left"></div>
    <div class="topbar-item" style="left:85px"><svg width="13" height="13" viewBox="0 0 24 24"><path d="M6.6 10.8a15 15 0 0 0 6.6 6.6l2.2-2.2c.3-.3.7-.4 1-.2 1.1.4 2.3.6 3.6.6.6 0 1 .4 1 1V20c0 .6-.4 1-1 1A17 17 0 0 1 3 4c0-.6.4-1 1-1h3.5c.6 0 1 .4 1 1 0 1.3.2 2.5.6 3.6.1.3 0 .7-.2 1z"/></svg>01 555 0142</div>
    <div class="topbar-item" style="left:214px"><svg width="13" height="13" viewBox="0 0 24 24"><path d="M2 5h20v2l-10 6L2 7zM2 9l10 6 10-6v10H2z"/></svg>info@brightfold-partners.example</div>
    <div class="topbar-item" style="left:643px"><svg width="13" height="13" viewBox="0 0 24 24"><path d="M12 2a7 7 0 0 0-7 7c0 5 7 13 7 13s7-8 7-13a7 7 0 0 0-7-7zm0 9.5a2.5 2.5 0 1 1 0-5 2.5 2.5 0 0 1 0 5z"/></svg>14 Harbour Row, Millbrook, Dublin 4, D04 KT21</div>
    <div class="topbar-sep"></div>
    <div class="topbar-soc" style="left:1074px"></div>
    <div class="topbar-soc" style="left:1100px"></div>
  </div>

  <!-- header -->
  <header class="abs header">
    <div class="abs brand" style="top:18px;left:85px">
      <div class="dot"></div>
      <div class="name">BRIGHTFOLD<br>PARTNERS</div>
    </div>
    <nav class="abs nav">
      <a class="active">Home</a><a>Who We Are</a><a>What We Do</a><a>How We Do</a><a>Contact</a>
    </nav>
    <div class="abs round-btn" style="left:1023px"><svg width="14" height="14" viewBox="0 0 24 24" fill="none" stroke="#2a2a2a" stroke-width="2.5"><circle cx="10" cy="10" r="7"/><path d="M15 15l6 6"/></svg></div>
    <div class="abs round-btn" style="left:1073px"><svg width="16" height="14" viewBox="0 0 24 20" fill="none" stroke="#2a2a2a" stroke-width="2.5"><path d="M2 3h20M2 10h14M2 17h20"/></svg></div>
  </header>
  <div class="abs band"></div>

  <!-- hero -->
  <section class="abs hero">
    <div class="abs hero-photo" role="img" aria-label="Businessman celebrating with arm raised, blended with a city skyline"></div>
    <div class="abs kicker">Brightfold Partners</div>
    <h1 class="abs">Data Analytics &amp;<br>Epm Consulting Services</h1>
    <div class="abs rule" style="top:275px;left:85px;width:56px"></div>
    <p class="abs">BP are a Data Analytics &amp; EPM company, specialising in the implementation and support of Business Intelligence, EPM and Data Analytics business solutions, both in the Cloud and on-premise.</p>
    <div class="abs play" style="top:384px;left:85px"><svg width="12" height="14" viewBox="0 0 12 14"><path d="M0 0l12 7-12 7z" fill="#e0865a"/></svg></div>
    <div class="abs btn" style="top:384px;left:152px;width:120px;height:46px">Learn More</div>
  </section>

  <!-- about -->
  <section class="about">
    <div class="abs about-back" role="img" aria-label="Hand pointing at financial charts on a screen"></div>
    <div class="abs about-front"><div role="img" aria-label="Support agent wearing a headset"></div></div>
    <div class="abs play-sq"><svg width="10" height="12" viewBox="0 0 12 14"><path d="M0 0l12 7-12 7z" fill="#fff"/></svg></div>
    <div class="abs label" style="top:873px;left:624px">Who We Are</div>
    <h2 class="abs section-h" style="top:898px;left:624px">Welcome to<br>Brightfold Partners</h2>
    <p class="abs body-text" style="top:1006px;left:624px;width:460px">Brightfold Partners is an exciting start-up in the Data Analytics and EPM space.&nbsp; Founded in 2019, BP specialise in the implementation and support of BI, EPM and Data Analytics business solutions, both in the Cloud and on-premise.</p>
    <p class="abs body-text" style="top:1103px;left:624px;width:460px">Call us on 01 555 0142 or email: info@brightfold-partners.example for more information</p>
    <div class="abs btn-outline" style="top:1164px;left:624px;width:151px;height:48px">Get Free Quote</div>
    <div class="abs partner" style="top:1173px;left:796px">Corvane<span class="bar"></span><span style="font-size:13px">Partner</span></div>
  </section>

  <!-- services -->
  <section class="abs services"></section>
  <div class="abs label" style="top:1474px;left:85px">What We Do</div>
  <h2 class="abs section-h" style="top:1498px;left:85px">Our Services</h2>
  <p class="abs body-text" style="top:1477px;left:590px;width:525px">We are passionate about data and making a difference for our clients by working in partnership with them, helping them on their journey to becoming an Brightfold Partner.</p>

  <article class="abs card" style="left:85px">
    <div class="img" role="img" aria-label="Handshake over a desk with laptop and model house" style="background:linear-gradient(135deg,#cfd4d8,#9aa3aa 55%,#b26a45)"></div>
    <div class="ico"><svg width="30" height="30" viewBox="0 0 24 24" fill="none" stroke="#e0865a" stroke-width="1.3"><rect x="8" y="3" width="12" height="8" rx="1"/><path d="M3 18h5l4 2 7-4-2-1-5 2M3 14h4l3 2"/></svg></div>
    <h3>Advise &amp;<br>Architect services</h3>
    <p>Helping our customers understand the art of the possible and safeguarding their investments by overseeing implementations.</p>
    <div class="more">Learn More<span><svg width="22" height="12" viewBox="0 0 22 12" fill="none" stroke="#fff" stroke-width="2"><path d="M0 6h20M15 1l5 5-5 5"/></svg></span></div>
  </article>
  <article class="abs card" style="left:438px">
    <div class="img" role="img" aria-label="Designers working over colourful wireframe sketches" style="background:linear-gradient(135deg,#e6ecf2,#9fb4cc 50%,#e08a5a)"></div>
    <div class="ico"><svg width="28" height="28" viewBox="0 0 24 24" fill="none" stroke="#e0865a" stroke-width="1.3"><rect x="3" y="5" width="16" height="15"/><path d="M6 16l4-4 3 3 5-7M20 3l1 1-7 7"/></svg></div>
    <h3>Design<br>&amp; Implement</h3>
    <p>Working with the project management team, through each stage of the project, with clearly defined deliverables and well exercised plans to deliver them.</p>
    <div class="more">Learn More<span><svg width="22" height="12" viewBox="0 0 22 12" fill="none" stroke="#fff" stroke-width="2"><path d="M0 6h20M15 1l5 5-5 5"/></svg></span></div>
  </article>
  <article class="abs card" style="left:788px">
    <div class="img" role="img" aria-label="Hands on a laptop keyboard with glowing digital overlay" style="background:linear-gradient(135deg,#4a5560,#2b333b 60%,#6b7884)"></div>
    <div class="ico"><svg width="28" height="28" viewBox="0 0 24 24" fill="none" stroke="#e0865a" stroke-width="1.3"><circle cx="12" cy="12" r="8"/><circle cx="12" cy="12" r="5"/><path d="M10 10l-2 2 2 2M14 10l2 2-2 2"/></svg></div>
    <h3>Optimise &amp;<br>Manage</h3>
    <p>Our Managed Services delivers proactive, on-demand support for EPM and Data Analytics environments</p>
    <div class="more">Learn More<span><svg width="22" height="12" viewBox="0 0 22 12" fill="none" stroke="#fff" stroke-width="2"><path d="M0 6h20M15 1l5 5-5 5"/></svg></span></div>
  </article>

  <!-- process -->
  <section class="abs process">
    <div class="abs process-side"></div>
    <div class="abs deco" style="top:-20px;left:1010px;width:70px;height:40px"></div>
    <div class="abs deco" style="top:47px;left:549px;width:34px;height:34px"></div>
    <div class="abs process-img" role="img" aria-label="Laptop showing an analytics dashboard with charts"></div>
    <div class="abs label" style="top:108px;left:587px">How We Do It</div>
    <h2 class="abs section-h" style="top:140px;left:587px">Our Working Process</h2>
    <div class="abs step" style="top:220px"><div class="num"><i></i><b>1</b></div><div>Rarem dolor sit amet conse ctetur adipiscing elit sed do eiusd tempor incididunt ut labore</div></div>
    <div class="abs step-line" style="top:283px"></div>
    <div class="abs step" style="top:318px"><div class="num"><i></i><b>2</b></div><div>Lorem Ipsum is simply dummy text of the printing and typesetting industry.</div></div>
    <div class="abs step-line" style="top:380px"></div>
    <div class="abs step" style="top:411px"><div class="num"><i></i><b>3</b></div><div>Lorem Ipsum has been the industry's standard dummy text ever since the 1500s</div></div>
  </section>

  <!-- contact -->
  <div class="abs label" style="top:2857px;left:85px">Contact Us</div>
  <h2 class="abs section-h" style="top:2883px;left:85px">Get in Touch</h2>
  <div class="abs contact-item" style="top:2957px"><svg width="24" height="24" viewBox="0 0 24 24"><path d="M12 2a7 7 0 0 0-7 7c0 5 7 13 7 13s7-8 7-13a7 7 0 0 0-7-7zm0 9.5a2.5 2.5 0 1 1 0-5 2.5 2.5 0 0 1 0 5z"/></svg><div>Location: 14 Harbour Row, Millbrook,<br>Dublin 4, D04 KT21</div></div>
  <div class="abs contact-item" style="top:3019px"><svg width="24" height="24" viewBox="0 0 24 24"><path d="M2 5h20v2l-10 6L2 7zM2 9l10 6 10-6v10H2z"/></svg><div>Email:<br>info@brightfold-partners.example</div></div>
  <div class="abs contact-item" style="top:3078px"><svg width="24" height="24" viewBox="0 0 24 24"><path d="M6.6 10.8a15 15 0 0 0 6.6 6.6l2.2-2.2c.3-.3.7-.4 1-.2 1.1.4 2.3.6 3.6.6.6 0 1 .4 1 1V20c0 .6-.4 1-1 1A17 17 0 0 1 3 4c0-.6.4-1 1-1h3.5c.6 0 1 .4 1 1 0 1.3.2 2.5.6 3.6.1.3 0 .7-.2 1z"/></svg><div>Phone:<br>01 555 0142</div></div>

  <form class="abs form">
    <h3>Book an Appointment</h3>
    <div class="rule"></div>
    <div class="field" style="top:109px;left:44px">First name*</div>
    <div class="field" style="top:109px;left:300px">Last name*</div>
    <div class="field" style="top:159px;left:44px">Phone number*</div>
    <div class="field" style="top:159px;left:300px">Email*</div>
    <div class="field" style="top:218px;left:44px;width:500px;height:76px">Message</div>
    <div class="btn send">Send Now</div>
  </form>

  <!-- footer -->
  <footer class="abs footer">
    <div class="abs brand" style="top:84px;left:87px;gap:10px">
      <div class="dot"></div>
      <div class="name">BRIGHTFOLD<br>PARTNERS</div>
    </div>
    <p class="abs" style="top:143px;left:87px;width:270px">We deliver insights which give our clients a competitive edge and a much deeper understanding of their organisation.</p>
    <div class="abs fsq" style="top:218px;left:87px"></div>
    <div class="abs fsq" style="top:218px;left:143px"></div>

    <h4 class="abs" style="top:73px;left:416px">Main Menu</h4>
    <div class="abs flink" style="top:132px;left:418px">Home</div>
    <div class="abs flink" style="top:165px;left:418px">Who We Are</div>
    <div class="abs flink" style="top:198px;left:418px">What We Do</div>
    <div class="abs flink" style="top:232px;left:418px">How We Do</div>
    <div class="abs flink" style="top:265px;left:418px">Contact</div>

    <h4 class="abs" style="top:73px;left:596px">Our Services</h4>
    <div class="abs flink" style="top:132px;left:598px">Advise &amp; Architect</div>
    <div class="abs flink" style="top:165px;left:598px">Design &amp; Implement</div>
    <div class="abs flink" style="top:198px;left:598px">Optimise &amp; Manage</div>

    <h4 class="abs" style="top:73px;left:822px">Contact</h4>
    <p class="abs" style="top:131px;left:823px;font-size:13.5px">Call : 01 555 0142</p>
    <p class="abs" style="top:164px;left:823px;font-size:13.5px">Email : info@brightfold-partners.example</p>
    <p class="abs" style="top:198px;left:823px;width:300px;font-size:13.5px">Location : 14 Harbour Row, Millbrook, Dublin 4, D04 KT21</p>
  </footer>
  <div class="abs copy-line"></div>
  <div class="abs copy">Copyright © 2022 <span>Brightfold-Partners</span>.All Rights Reserved.</div>

</div>
</body>
</html>
```